Flyer Design Project for Brightwater Wellbeing Rooms

We are a psychology clinic that specialises in eating, parenting and chronic illness & pain. See our website for a summary.

We need a flyer that will go to doctors and schools in the local area.

Things to include on the front page:

Immediate appointments available
After hours appointments available
Male and female psychologists

Phone 9563 2190
Web brightwaterwellbeingrooms.com.au

On the back page:

Phone 9563 2190
Suite 1/1287 Marlowe Rd, Kelverton East 3185.
brightwaterwellbeingrooms.com.au

Parenting: Parenthood is an amazing journey, but for lots of people it raises all sorts of issues from fear of birth, breastfeeding difficulties and settling problems, to toddler discipline and food fussiness all the way through to getting help for your depressed or anxious adolescent. Our Parenting Psychologists can help you be the best parent you can be which will in turn lead to happier families, homes, children and parents.

Chronic illness/pain: Diabetes, heart disease, arthritis, asthma, migraines, dizziness, chronic fatigue syndrome, infertility, and PCOS are just some of the conditions that can be managed with psychological interventions. Everything we do is about helping you to manage your condition and get back to focusing on what you really want your life to be about.

Eating: Whether you suffer from anorexia, bulimia or binge eating, our strategies help you develop a healthy relationship with food and your body. The practical tips and strategies that we can provide are very useful for people undergoing lapband surgery or liposuction.

I am interested in whether the photographs that I have already purchased can be used...so please have a look through the website and see which you think will suit your design. Photographs are not absolutely necessary though, so if it doesn't fit with your idea that is okay too.
Updates

HI Everyone,

Thanks for submitting so far! I haven't found anything yet that has hit the mark. And I am thinking that is my fault and maybe that way i have described what I want. I apologise and hope that this update might help.

This brochure is likely to sit with lots of other brochures in a doctors waiting room so it needs to be different - so that it will be noticed.

The majority of our market are women - so something feminine is important. Maybe it needs to be a little more playful that I had initially thought. Like maybe not your standard blocky text and bolds and primary colours. But something more creative, more personal.

I want to not focus just on the family theme. Parenting is one area that we cover, but also we help people with eating disorders and chronic illness/chronic pain. So the photographs that I use need to be more general. It is importnat to focus on happy and healthy looking people. As we went to appeal to what my potential clients want to look like and feel like.

I do hope this helps to guide you. I promise that once I see a flyer that I could choose, I will turn the funding to guaranteed. I did this last time...I am just a bit nervous as I haven't received anything yet that I am excited about.

Kindest regards,

Marnie.

Hi Everyone,

Thank you for your designs coming in! As promised, as soon as I received a design that I could see myself choosing I would change the status from refundable to committed. I have now done this!

I have received a design that I would say is good. It is not perfect however...so please keep the ideas coming.

To give more direction, the one that came in has a nice theme that runs through the brochure. Not too many different types of font and colours detracting from the flow of the flyer. However, the thing that I am concerned about is whether it will stand out enough on a rack of other flyers in a doctors waiting room.

I hope this helps with your creative ideas.

Thanks again to everyone!

Marnie.

Thanks SO much to everyone who is putting in designs. You are making my decision difficult!

I am wondering if you can update your designs with a few things:

can I ask you to make some text changes:

1. Can we have a heading on the front page: Psychologists  and then can you put Kelverton East in smaller writing just below it?

2. Id like to say on the front: Specialising in parenting, disordered eating and chronic pain & illness

3. Delete Male & Female Psychologists

4. In general we dont' need to have the logo standing out. We don't have a well known brand yet, so I am not wanting to take up valuable space with this - so perhaps it shoudl be small and maybe just on the back? Keeping the name of our clinic on the front with the website shoudl be sufficient.

Thanks heaps everyone...I will make decision very soon!

Target Market(s)

20-40 year olds. Working. Educated. Female. They might have a family/children.
Australian. Engish speaking.

Industry/Entity Type

Clinic

Requirements
Must have
• I would like to include our logo. Please do not use the colour green that it is in. I hate that colour! but I LOVE the logo.

I would like to follow through with some of the themes of the website and other stationary.

I will attach some of the other stationary I have had designed.

I really like the colours in the letterhead - especially that blue of the logo.

I think it needs to have a dash of colour with it at least...something that will stand out and be noticed on a brochure rack...but also have a look of class/sophistication/modern.
Nice to have
• Perhaps photograph of happy and healthy people.
Should not have
• I don't like bold text or too many different types of fonts.

It shouldn't look too cluttered so I might need to reduce the text I have included - I will need to see it first.

```html
<!DOCTYPE html>
<html lang="en">
<head>
<meta charset="utf-8">
<title>Brightwater Wellbeing Rooms – Flyer</title>
<link rel="stylesheet" href="https://fonts.googleapis.com/css2?family=Bebas+Neue&family=Varela+Round&display=swap">
<style>
  :root {
    --teal-top: #63d2ca;
    --teal-title: #4fb2a9;
    --teal-deep: #3a8f87;
    --teal-light: #86d9d1;
    --charcoal: #3a3e40;
    --ink: #2e3233;
    --white: #ffffff;
    --stripe-1: #8fd7a8;
    --stripe-2: #9fe0d9;
    --stripe-3: #6fb8b0;
    --stripe-4: #6e8690;
    --stripe-5: #2f7f76;
    --stripe-6: #5cc7be;
    --stripe-7: #343a3c;
    --stripe-8: #a69b6a;
  }
  * { margin: 0; padding: 0; box-sizing: border-box; }
  html, body { width: 848px; height: 1200px; overflow: hidden; background: var(--white); }
  .flyer { position: relative; width: 848px; height: 1200px; overflow: hidden; background: var(--white); font-family: "Varela Round", sans-serif; }

  .top-band { position: absolute; left: 0; top: 0; width: 848px; height: 59px; background: var(--teal-top); }
  .stripe { position: absolute; display: flex; height: 7px; z-index: 2; }
  .stripe span { flex: 1; }
  .stripe--top { left: 0; top: 59px; width: 848px; }
  .stripe--lower { left: 558px; top: 804px; width: 290px; }

  .site-line { position: absolute; left: 67px; top: 80px; font-size: 15px; color: var(--ink); }
  .site-line .url-accent { color: var(--teal-title); }

  .photo-grid { position: absolute; left: 67px; top: 119px; }

  .clinic-title { position: absolute; left: 370px; top: 556px; font-size: 48px; line-height: 60px; color: var(--teal-title); font-weight: 400; }

  .lower-panel { position: absolute; left: 0; top: 803px; width: 848px; height: 397px; overflow: hidden;
    background: radial-gradient(ellipse 65% 75% at 50% 40%, var(--teal-light) 0%, #5fbdb5 45%, var(--teal-deep) 100%); }
  .panel-ring { position: absolute; left: 540px; top: 70px; }

  .offer-band { position: absolute; left: 0; top: 772px; width: 558px; height: 172px; background: var(--charcoal);
    clip-path: polygon(0 0, 100% 0, 94.4% 100%, 0 100%); }
  .offer-list { list-style: none; position: absolute; left: 47px; top: 786px; font-family: "Bebas Neue", sans-serif;
    font-size: 36px; line-height: 55px; color: var(--white); letter-spacing: 0.5px; }

  .clinic-mark { position: absolute; left: 108px; top: 996px; display: flex; align-items: center; gap: 24px; }
  .clinic-mark .dot { width: 84px; height: 84px; border: 3px solid var(--white); border-radius: 50%; }
  .clinic-mark .name { font-size: 24px; line-height: 29px; letter-spacing: 2px; color: var(--white); text-transform: uppercase; }

  .phone { position: absolute; left: 119px; top: 1104px; font-family: "Bebas Neue", sans-serif; font-size: 55px; line-height: 56px; color: var(--white); letter-spacing: -0.3px; }
</style>
</head>
<body>
<main class="flyer">
  <div class="top-band"></div>
  <div class="stripe stripe--top">
    <span style="background:var(--stripe-1)"></span><span style="background:var(--stripe-2)"></span>
    <span style="background:var(--stripe-3)"></span><span style="background:var(--stripe-4)"></span>
    <span style="background:var(--stripe-5)"></span><span style="background:var(--stripe-6)"></span>
    <span style="background:var(--stripe-7)"></span><span style="background:var(--stripe-8)"></span>
  </div>

  <p class="site-line">Visit our site at www.<span class="url-accent">brightwaterwellbeingrooms</span>.com.au</p>

  <svg class="photo-grid" width="715" height="571" viewBox="0 0 715 571" role="img" aria-label="Photo of a smiling mother and her toddler playing on green grass in a sunny park, shown across a grid of tiles">
    <defs>
      <linearGradient id="parkGreens" x1="0" y1="0" x2="715" y2="571" gradientUnits="userSpaceOnUse">
        <stop offset="0" stop-color="#6f9f45"/>
        <stop offset="0.45" stop-color="#a9c98a"/>
        <stop offset="0.7" stop-color="#8fc25a"/>
        <stop offset="1" stop-color="#5f9a3a"/>
      </linearGradient>
      <radialGradient id="sunlitHaze" cx="600" cy="40" r="260" gradientUnits="userSpaceOnUse">
        <stop offset="0" stop-color="#eef2e6" stop-opacity="0.9"/>
        <stop offset="1" stop-color="#eef2e6" stop-opacity="0"/>
      </radialGradient>
      <radialGradient id="warmCentre" cx="290" cy="300" r="240" gradientUnits="userSpaceOnUse">
        <stop offset="0" stop-color="#c99a86" stop-opacity="0.85"/>
        <stop offset="0.55" stop-color="#8aa0b4" stop-opacity="0.45"/>
        <stop offset="1" stop-color="#8aa0b4" stop-opacity="0"/>
      </radialGradient>
      <clipPath id="tiles">
        <rect x="0" y="0" width="139" height="139"/><rect x="144" y="0" width="139" height="139"/>
        <rect x="288" y="0" width="139" height="139"/><rect x="432" y="0" width="139" height="139"/>
        <rect x="576" y="0" width="139" height="139"/>
        <rect x="0" y="144" width="139" height="139"/><rect x="144" y="144" width="139" height="139"/>
        <rect x="288" y="144" width="139" height="139"/><rect x="432" y="144" width="139" height="139"/>
        <rect x="576" y="144" width="139" height="139"/>
        <rect x="0" y="288" width="139" height="139"/><rect x="144" y="288" width="139" height="139"/>
        <rect x="288" y="288" width="139" height="139"/><rect x="432" y="288" width="139" height="139"/>
        <rect x="576" y="288" width="139" height="139"/>
        <rect x="0" y="432" width="139" height="139"/><rect x="144" y="432" width="139" height="139"/>
      </clipPath>
    </defs>
    <g clip-path="url(#tiles)">
      <rect width="715" height="571" fill="url(#parkGreens)"/>
      <rect width="715" height="571" fill="url(#sunlitHaze)"/>
      <rect width="715" height="571" fill="url(#warmCentre)"/>
    </g>
  </svg>

  <h1 class="clinic-title">Brightwater<br>Wellbeing Rooms</h1>

  <section class="lower-panel">
    <svg class="panel-ring" width="420" height="420" viewBox="0 0 420 420" aria-hidden="true">
      <circle cx="210" cy="210" r="190" fill="none" stroke="var(--white)" stroke-width="16"/>
    </svg>
  </section>
  <div class="stripe stripe--lower">
    <span style="background:var(--stripe-2)"></span><span style="background:var(--stripe-7)"></span>
    <span style="background:var(--stripe-8)"></span>
  </div>

  <div class="offer-band"></div>
  <ul class="offer-list">
    <li>- Immediate appointments available</li>
    <li>- After hours appointments available</li>
    <li>- Male and female psychologists</li>
  </ul>

  <div class="clinic-mark">
    <span class="dot"></span>
    <span class="name">Brightwater<br>Wellbeing<br>Rooms</span>
  </div>

  <p class="phone">Phone: 9563 2190</p>
</main>
</body>
</html>
```